Bluegate Physiotherapy
Business Cards, Stationary, Letterhead, Magnet, Presentation Folder, A5 Referral Pad, Email Signatur
Bluegate Physiotherapy -
Creative Brief
Professional
Tom Ellingsworth
BSc Physiotherapy / Acupuncturist / Cert IV Occupational Health & Safety
Unit 3, 48 Kestrel Lane, Mandurah WA 6210
tom.ellingsworth@bluegatephysio-example.com.au
www.bluegatephysio-example.com.au
Magnet to be standard business card size (portrait OR landscape) and include only phone, address and website (in addition to graphic component). Referral pad to be A5 size. At the TOP: "Patient Name", "Date" as well as 4 tick boxes "W.C.", "Vet. Affairs", "Private" "EPC". At the BOTTOM: "Referring Doctor" "Sign" "Doctors Name" and "Address" as well as "Preferred Contact" with 4 tick boxes "E-mail", "Phone", "Fax", "Snail Mail". Down one SIDE to have a list: "Manual Therapy", "Massage", "Exercise Prescription", "Gym Based Rehab", "Workplace Assessment", "Ergonomics", "Acupuncture", "Sports Physiotherapy", "Womens Health".

```html
<!DOCTYPE html>
<html lang="en">
<head>
<meta charset="utf-8">
<title>Bluegate Physiotherapy – Stationery Suite</title>
<link rel="stylesheet" href="https://fonts.googleapis.com/css2?family=Arimo:wght@400;700&display=swap">
<style>
  :root{
    --board:#2a2b2d;
    --paper:#ffffff;
    --blue-deep:#062a63;
    --blue-mid:#0b4a9c;
    --blue-light:#2a7fd0;
    --ink:#1d2a44;
    --muted:#8a8f98;
    --label:#9aa0a8;
    --green:#5bb432;
    --yellow:#f2c313;
    --orange:#ee7d1c;
    --red:#d9342b;
  }
  *{box-sizing:border-box;margin:0;padding:0}
  html,body{width:1200px;height:343px;overflow:hidden;background:var(--board)}
  body{font-family:"Arimo",Arial,sans-serif;color:var(--ink);position:relative}
  .item{position:absolute}
  .label{position:absolute;font-size:5px;color:var(--label);letter-spacing:.2px;white-space:nowrap}
  .paper{background:var(--paper);box-shadow:0 2px 6px rgba(0,0,0,.45)}
  .blue{background:radial-gradient(ellipse at 60% 30%,var(--blue-light),var(--blue-mid) 45%,var(--blue-deep))}
  .stripe{height:3px;background:linear-gradient(90deg,var(--green),var(--yellow),var(--orange),var(--red))}
  .brand{display:flex;align-items:center;gap:3px;font-weight:700;color:var(--blue-mid);white-space:nowrap}
  .brand .dot{border-radius:50%;background:var(--blue-mid);flex:none}
  .brand.on-blue{color:#fff}
  .brand.on-blue .dot{background:#fff}
  .tiny{font-size:3.6px;line-height:1.45;color:var(--muted)}
  .leaf-art{position:absolute;background:radial-gradient(ellipse at 50% 80%,rgba(90,170,255,.45),rgba(10,60,140,0) 70%)}

  /* folder */
  .folder-front{left:86px;top:28px;width:250px;height:292px}
  .folder-front .head{height:70px;padding:16px 0 0 70px}
  .folder-front .head .brand{font-size:13px}
  .folder-front .head .brand .dot{width:14px;height:14px}
  .folder-front .body{position:absolute;left:0;right:0;top:70px;bottom:0}
  .folder-front .leaf-art{left:60px;top:10px;width:150px;height:200px}
  .folder-pocket{left:8px;top:236px;width:150px;height:88px}
  .folder-pocket .slot{position:absolute;left:56px;top:22px;width:30px;height:8px;border-radius:4px;background:var(--paper)}
  .folder-pocket .tiny{position:absolute;left:10px;top:40px}
  .folder-tab{left:8px;top:200px;width:40px;height:36px;background:var(--paper);box-shadow:0 2px 6px rgba(0,0,0,.4)}

  /* envelope */
  .envelope-back{left:368px;top:160px;width:320px;height:140px;overflow:hidden}
  .envelope-back .flap{position:absolute;inset:0}
  .envelope-front{left:400px;top:172px;width:300px;height:126px}
  .envelope-front .brand{position:absolute;left:10px;top:10px;font-size:7px}
  .envelope-front .brand .dot{width:7px;height:7px}
  .envelope-front .window{position:absolute;left:30px;top:62px;width:84px;height:22px;border:1px solid #d6dbe2;border-radius:2px}
  .envelope-front .corner{position:absolute;right:0;bottom:0;width:70px;height:126px}

  /* business card */
  .card{left:512px;top:172px;width:76px;height:124px;padding:8px 6px}
  .card .brand{font-size:5.2px}
  .card .brand .dot{width:6px;height:6px}
  .card .call{margin-top:34px;font-size:4px;color:#cfe0f5}
  .card .phone{font-size:13px;font-weight:700;color:#fff;letter-spacing:.3px}
  .card .tiny{color:#cfe0f5;margin-top:8px}

  /* magnet */
  .magnet{left:612px;top:240px;width:110px;height:70px;padding:7px}
  .magnet .brand{font-size:5.5px}
  .magnet .brand .dot{width:6px;height:6px}
  .magnet .tiny{color:#d6e4f6;margin-top:20px}

  /* email signature */
  .email-sig{left:600px;top:24px;width:200px;height:44px;padding:6px 8px}
  .email-sig .brand{font-size:6px}
  .email-sig .brand .dot{width:6px;height:6px}
  .email-sig .tiny{margin-top:4px}
  .email-sig .stripe{position:absolute;left:0;right:0;bottom:0;height:2px}

  /* compliments slip */
  .compliments{left:712px;top:84px;width:130px;height:118px;padding:8px}
  .compliments .brand{font-size:6px}
  .compliments .brand .dot{width:6px;height:6px}
  .compliments .title{font-size:6px;color:var(--blue-mid);margin-top:18px;font-weight:700}
  .compliments .tiny{margin-top:3px}
  .compliments .stripe{position:absolute;left:0;right:0;bottom:0}

  /* letterhead */
  .letterhead{left:850px;top:28px;width:132px;height:296px;padding:10px}
  .letterhead .brand{font-size:7px}
  .letterhead .brand .dot{width:7px;height:7px}
  .letterhead .tiny{margin-top:6px}
  .letterhead .lines{margin-top:18px}
  .letterhead .lines span{display:block;height:1px;background:#eceef2;margin-bottom:7px}
  .letterhead .stripe{position:absolute;left:0;right:0;bottom:0}

  /* referral pad */
  .referral{left:994px;top:24px;width:194px;height:300px;padding:10px;font-size:4.2px}
  .referral .top{display:flex;justify-content:space-between;align-items:flex-start}
  .referral .brand{font-size:7px}
  .referral .brand .dot{width:7px;height:7px}
  .referral .field{border-bottom:.6px solid #c9ced6;padding:5px 0 1px;color:var(--ink)}
  .referral .ticks{display:flex;gap:8px;margin-top:5px}
  .referral .services{margin-top:10px;width:80px}
  .referral .services li{list-style:none;display:flex;align-items:center;gap:3px;margin-bottom:4.5px}
  .box{display:inline-block;width:4px;height:4px;border:.6px solid #8a93a2;flex:none}
  .referral .doctor{position:absolute;left:10px;right:10px;bottom:14px;padding-top:4px;border-top:.8px solid var(--blue-mid)}
  .referral .doctor .head{font-weight:700;color:var(--blue-mid)}
  .referral .stripe{position:absolute;left:0;right:0;bottom:0}
</style>
</head>
<body>

<span class="label" style="left:86px;top:16px">Presentation Folder</span>
<span class="label" style="left:600px;top:14px">Email Signature</span>
<span class="label" style="left:712px;top:74px">Compliments Slip</span>
<span class="label" style="left:850px;top:18px">Letterhead</span>
<span class="label" style="left:994px;top:14px">Referral Pad</span>
<span class="label" style="left:368px;top:304px">Envelope DL</span>
<span class="label" style="left:512px;top:164px">Business Card</span>
<span class="label" style="left:612px;top:314px">Magnet</span>

<!-- Presentation folder -->
<div class="item folder-tab"></div>
<section class="item folder-front paper">
  <div class="head"><div class="brand"><span class="dot"></span>Bluegate Physiotherapy</div></div>
  <div class="body blue">
    <div class="leaf-art" role="img" aria-label="Soft leaf graphic rising from the bottom of the folder"></div>
  </div>
</section>
<section class="item folder-pocket blue">
  <span class="slot"></span>
  <p class="tiny" style="color:#cfe0f5">Unit 3, 48 Kestrel Lane, Mandurah WA 6210<br>www.bluegatephysio-example.com.au</p>
</section>

<!-- Envelope -->
<div class="item envelope-back blue">
  <svg class="flap" viewBox="0 0 320 140" preserveAspectRatio="none">
    <path d="M0 0 L160 70 L320 0" fill="none" stroke="rgba(255,255,255,.25)" stroke-width="1"/>
  </svg>
</div>
<section class="item envelope-front paper">
  <div class="brand"><span class="dot"></span>Bluegate Physiotherapy</div>
  <div class="window"></div>
  <div class="corner blue" role="img" aria-label="Blue leaf graphic panel"></div>
</section>

<!-- Business card -->
<section class="item card blue">
  <div class="brand on-blue"><span class="dot"></span>Bluegate Physiotherapy</div>
  <p class="call">Call us today</p>
  <p class="phone">9555 0142</p>
  <p class="tiny">Unit 3, 48 Kestrel Lane<br>Mandurah WA 6210</p>
</section>

<!-- Magnet -->
<section class="item magnet blue">
  <div class="brand on-blue"><span class="dot"></span>Bluegate Physiotherapy</div>
  <p class="tiny">9555 0142<br>Unit 3, 48 Kestrel Lane, Mandurah WA 6210<br>www.bluegatephysio-example.com.au</p>
</section>

<!-- Email signature -->
<section class="item email-sig paper">
  <div class="brand"><span class="dot"></span>Bluegate Physiotherapy</div>
  <p class="tiny">Tom Ellingsworth · tom.ellingsworth@bluegatephysio-example.com.au</p>
  <div class="stripe"></div>
</section>

<!-- Compliments slip -->
<section class="item compliments paper">
  <div class="brand"><span class="dot"></span>Bluegate Physiotherapy</div>
  <p class="title">With Compliments</p>
  <p class="tiny">Unit 3, 48 Kestrel Lane, Mandurah WA 6210<br>www.bluegatephysio-example.com.au</p>
  <div class="stripe"></div>
</section>

<!-- Letterhead -->
<section class="item letterhead paper">
  <div class="brand"><span class="dot"></span>Bluegate Physiotherapy</div>
  <p class="tiny">Tom Ellingsworth<br>BSc Physiotherapy / Acupuncturist<br>Unit 3, 48 Kestrel Lane, Mandurah WA 6210<br>tom.ellingsworth@bluegatephysio-example.com.au</p>
  <div class="lines"><span></span><span></span><span></span><span></span><span></span><span></span><span></span><span></span><span></span></div>
  <div class="stripe"></div>
</section>

<!-- Referral pad -->
<section class="item referral paper">
  <div class="top">
    <div class="brand"><span class="dot"></span>Bluegate Physiotherapy</div>
    <p class="tiny" style="text-align:right">9555 0142<br>www.bluegatephysio-example.com.au</p>
  </div>
  <p class="field">Patient Name</p>
  <p class="field">Date</p>
  <div class="ticks">
    <span><span class="box"></span> W.C.</span>
    <span><span class="box"></span> Vet. Affairs</span>
    <span><span class="box"></span> Private</span>
    <span><span class="box"></span> EPC</span>
  </div>
  <ul class="services">
    <li><span class="box"></span>Manual Therapy</li>
    <li><span class="box"></span>Massage</li>
    <li><span class="box"></span>Exercise Prescription</li>
    <li><span class="box"></span>Gym Based Rehab</li>
    <li><span class="box"></span>Workplace Assessment</li>
    <li><span class="box"></span>Ergonomics</li>
    <li><span class="box"></span>Acupuncture</li>
    <li><span class="box"></span>Sports Physiotherapy</li>
    <li><span class="box"></span>Womens Health</li>
  </ul>
  <div class="doctor">
    <p class="head">Referring Doctor</p>
    <p class="field">Sign</p>
    <p class="field">Doctors Name</p>
    <p class="field">Address</p>
    <div class="ticks">
      <span style="font-weight:700">Preferred Contact</span>
      <span><span class="box"></span> E-mail</span>
      <span><span class="box"></span> Phone</span>
      <span><span class="box"></span> Fax</span>
      <span><span class="box"></span> Snail Mail</span>
    </div>
  </div>
  <div class="stripe"></div>
</section>

</body>
</html>
```